Visit card for Luxury Alpine home

Velvet Ridge Chalet (Hinterthal, Austria) – visit card

Brief: To design a visit card (4/4) that can be both left for existing guests and handed out to friends/business contacts to promote our luxury holiday home in the Austrian alps which can be rented year -round but primarily for summer (hiking/biking/golf) and winter (skiing). Primary focus is for family as its a 3br/3ba place that is usually booked for either a larger family or two families.

Basic information required/purpose: email/contact info. Basic information about the place, location, possibly some ideas/icons about what to do. Imagery that gives people the idea about luxury/fun/mountains etc. Hopefully the card would be something to interest them enough to check out the website and eventually make a direct booking with us.

Our details and photos:

https://velvetridgechalet.com
https://www.facebook.com/velvetridgechalet/

contact information for people to book:
stay.brenvale@larkpost.net
+420 604918352

some other resources:

http://www.tamrisberg-info.at/en/vacation.html
the moutains are called Hochkoenig and our village is Hinterthal which is next to Maria alm

Target Market(s)

European (winter) and Middle-Eastern (summer) families.

Industry/Entity Type

Travel

Contact Information for Business Card

standard 4/4 to be used for prospect

Font styles to use
Sans Serif

Colors

Designer to choose colors to be used in the design.

Requirements
Must have
• all relevant information for the client to contact us
• colorful/luxury imagery of the property (we can provide better photo quality that the web downloads)
Nice to have
• not particular about fonts. preferring subdued colours

```html
<!DOCTYPE html>
<html lang="en">
<head>
<meta charset="utf-8">
<title>Velvet Ridge Chalet – Visit Card</title>
<link href="https://fonts.googleapis.com/css2?family=Oswald:wght@400;500&family=Open+Sans:wght@300;400&display=swap" rel="stylesheet">
<style>
  :root {
    --backdrop: #d9d9d9;
    --card: #ffffff;
    --ink: #2b2b2b;
    --ink-soft: #4a4a4a;
    --accent: #3a78c2;
    --icon: #3c5d8a;
    --meadow: #7d9a57;
    --sky: #9db8d4;
    --snow: #e8edf2;
    --wood: #6b4a35;
    --interior: #8a7866;
    --kitchen: #cfcac3;
    --wool: #c8283a;
    --frost: #f1e6e8;
  }
  * { margin: 0; padding: 0; box-sizing: border-box; }
  html, body { width: 900px; height: 1200px; overflow: hidden; }
  body { background: var(--backdrop); position: relative; font-family: "Open Sans", sans-serif; }

  .card {
    position: absolute; left: 75px; width: 750px;
    background: var(--card); border-radius: 18px; overflow: hidden;
    box-shadow: 0 6px 14px rgba(0,0,0,.25);
  }
  .card--front { top: 135px; height: 450px; }
  .card--back { top: 630px; height: 444px; }

  .photo-row { position: absolute; left: 0; width: 100%; display: flex; gap: 4px; }
  .photo-row--top { top: 0; height: 165px; }
  .photo-row--bottom { bottom: 0; height: 186px; }
  .photo { height: 100%; }

  .photo--meadow { flex: 0 0 220px; background: linear-gradient(180deg, var(--sky) 0%, #dfe6ee 40%, var(--meadow) 70%, #5d7a3d 100%); }
  .photo--peaks { flex: 0 0 280px; background: linear-gradient(170deg, #a9bccf 0%, var(--snow) 45%, #8b96a3 80%, #5f6873 100%); }
  .photo--lounge { flex: 1; background: linear-gradient(180deg, #b7aa9a 0%, #7f6a58 60%, #4d3f33 100%); }
  .photo--facade { flex: 0 0 250px; background: linear-gradient(180deg, #c8d4df 0%, var(--wood) 45%, #4a3426 100%); }
  .photo--bedroom { flex: 0 0 240px; background: linear-gradient(180deg, #5c4a3e 0%, var(--interior) 55%, #d9d0c4 100%); }
  .photo--kitchen { flex: 1; background: linear-gradient(180deg, #efeeec 0%, var(--kitchen) 60%, #8c8276 100%); }

  .brand-band {
    position: absolute; top: 165px; left: 0; width: 100%; height: 99px;
    display: flex; flex-direction: column; align-items: center; justify-content: center;
  }
  .brand-name {
    font-family: "Oswald", sans-serif; font-weight: 400; font-size: 50px;
    line-height: 1; color: var(--ink); letter-spacing: .5px; text-transform: uppercase;
  }
  .brand-tagline {
    margin-top: 6px; font-size: 16px; color: var(--accent);
    text-transform: uppercase; letter-spacing: .3px;
  }

  .heart-photo {
    position: absolute; left: 0; top: 0; width: 480px; height: 100%;
    background:
      radial-gradient(ellipse 150px 140px at 190px 210px, var(--wool) 0%, #b11f30 55%, rgba(200,40,58,0) 100%),
      linear-gradient(90deg, var(--frost) 0%, #f6eef0 60%, rgba(255,255,255,0) 100%);
  }

  .back-details {
    position: absolute; right: 36px; top: 50px; text-align: right;
  }
  .back-details .brand-name { font-size: 38px; }
  .back-details .brand-tagline { font-size: 12px; margin-top: 4px; }
  .address {
    margin-top: 30px; font-weight: 300; font-size: 19px; line-height: 1.35; color: var(--ink-soft);
  }
  .contact-list { list-style: none; margin-top: 16px; }
  .contact-item {
    display: flex; justify-content: flex-end; align-items: center; gap: 10px;
    font-weight: 300; font-size: 19px; line-height: 1.55; color: var(--ink-soft);
  }
  .contact-icon { width: 20px; height: 20px; flex: 0 0 20px; }
</style>
</head>
<body>

<section class="card card--front">
  <div class="photo-row photo-row--top">
    <div class="photo photo--meadow" role="img" aria-label="Green alpine meadow below snowy peaks"></div>
    <div class="photo photo--peaks" role="img" aria-label="Snow-covered mountain range"></div>
    <div class="photo photo--lounge" role="img" aria-label="Apartment living room with sofa"></div>
  </div>

  <div class="brand-band">
    <h1 class="brand-name">Velvet Ridge Chalet</h1>
    <p class="brand-tagline">Luxury rental apartment in Hinterthal</p>
  </div>

  <div class="photo-row photo-row--bottom">
    <div class="photo photo--facade" role="img" aria-label="Wooden chalet building exterior"></div>
    <div class="photo photo--bedroom" role="img" aria-label="Bedroom with twin beds"></div>
    <div class="photo photo--kitchen" role="img" aria-label="Modern white kitchen"></div>
  </div>
</section>

<section class="card card--back">
  <div class="heart-photo" role="img" aria-label="Red knitted gloves forming a heart in the snow"></div>

  <div class="back-details">
    <h2 class="brand-name">Velvet Ridge Chalet</h2>
    <p class="brand-tagline">Luxury rental apartment in Hinterthal</p>
    <p class="address">Obere Lindenhang 12<br>Hinterthal</p>
    <ul class="contact-list">
      <li class="contact-item">stay.brenvale@larkpost.net
        <svg class="contact-icon" viewBox="0 0 20 20"><circle cx="10" cy="10" r="10" fill="var(--icon)"/><path d="M7 5.5l1.6 2.6-1 1.2a7 7 0 003.1 3.1l1.2-1 2.6 1.6-.8 1.8c-4 0-7.9-3.9-7.9-7.9z" fill="#fff"/></svg>
      </li>
      <li class="contact-item">+420 604918352
        <svg class="contact-icon" viewBox="0 0 20 20"><circle cx="10" cy="10" r="10" fill="var(--icon)"/><rect x="5" y="6.5" width="10" height="7" fill="none" stroke="#fff" stroke-width="1.3"/><path d="M5 6.5l5 4 5-4" fill="none" stroke="#fff" stroke-width="1.3"/></svg>
      </li>
      <li class="contact-item">www.velvetridgechalet.com
        <svg class="contact-icon" viewBox="0 0 20 20"><circle cx="10" cy="10" r="10" fill="var(--icon)"/><circle cx="10" cy="10" r="5" fill="none" stroke="#fff" stroke-width="1.2"/><path d="M5 10h10M10 5c-2.5 3-2.5 7 0 10M10 5c2.5 3 2.5 7 0 10" fill="none" stroke="#fff" stroke-width="1.1"/></svg>
      </li>
      <li class="contact-item">velvetridgechalet
        <svg class="contact-icon" viewBox="0 0 20 20"><circle cx="10" cy="10" r="10" fill="var(--icon)"/></svg>
      </li>
    </ul>
  </div>
</section>

</body>
</html>
```